Update the A4 Specials Page for Restaurant/Cafe

Provide a MINIMALIST attractive Specials page we can print weekly for our food and drink specials to give to our guests. Final design is to be provided in WORD Document so it can be easily edited by Manager. Should be black text and MINIMALIST to minimise ink usage as we print hundreds a week. We have UPLOADED the existing page as a template for you to update. Maybe logo can stay, see what you think. Or delete it and do something else. Keep it simple. Choose a good FONT. Could be a little playful with a cocktail ICON or something. Our existing menus can be seen at www.tallpinebistro.com.au and they are using font Alegreya. Please note we are unable to provide any feedback to designers, however we really do appreciate your time if you are submitting a design. Thank you for your participation.

```html
<!DOCTYPE html>
<html lang="en">
<head>
<meta charset="utf-8">
<title>Tall Pine Bistro – Weekly Specials</title>
<link rel="stylesheet" href="https://fonts.googleapis.com/css2?family=Fredoka:wght@600&family=Roboto+Condensed:wght@400;700&display=swap">
<style>
  :root {
    --backdrop: #eeeeef;
    --page: #ffffff;
    --ink: #111111;
    --tint: #f3f3f3;
    --tint-soft: #f8f8f8;
    --rule: #d6d6d6;
  }
  * { margin: 0; padding: 0; box-sizing: border-box; }
  html, body {
    width: 1200px; height: 1200px; overflow: hidden;
    background: var(--backdrop);
  }
  .menu-page {
    position: absolute; left: 216px; top: 56px;
    width: 765px; height: 1085px;
    background: var(--page);
    box-shadow: 0 6px 24px rgba(0,0,0,.12);
    overflow: hidden;
    font-family: "Roboto Condensed", "Arial Narrow", sans-serif;
    color: var(--ink);
  }
  .drink-photo {
    position: absolute; left: 400px; top: 760px; width: 365px; height: 325px;
    background: linear-gradient(180deg, var(--tint-soft) 0%, var(--tint) 100%);
  }
  .accent { position: absolute; background: var(--tint); }
  .accent-squiggle { left: 0; top: 0; width: 110px; height: 150px; border-radius: 0 0 55px 0; }
  .accent-splash { left: 612px; top: 268px; width: 40px; height: 40px; border-radius: 50%; }
  .accent-spiral { left: 680px; top: 440px; width: 80px; height: 90px; border-radius: 50%; }
  .accent-drops { left: 30px; top: 985px; width: 70px; height: 60px; border-radius: 50%; }

  .brand-name {
    position: absolute; left: 0; right: 0; top: 112px;
    text-align: center;
    font-weight: 700; font-size: 50px; line-height: 1.05;
    letter-spacing: 2px; text-transform: uppercase;
    color: var(--ink);
  }
  .specials-title {
    position: absolute; left: 0; right: 0; top: 300px;
    text-align: center;
    font-family: "Fredoka", "Comic Sans MS", sans-serif;
    font-weight: 600; font-size: 64px; line-height: 1;
    color: var(--ink);
  }
  .menu-item { position: absolute; left: 94px; width: 527px; }
  .item-line { display: flex; align-items: baseline; }
  .item-name { font-weight: 700; font-size: 22px; text-transform: uppercase; white-space: nowrap; }
  .item-leader { flex: 1; border-bottom: 2px dotted var(--ink); margin: 0 22px 0 12px; transform: translateY(-4px); }
  .item-price { font-weight: 700; font-size: 17px; width: 34px; text-align: left; }
  .item-desc { font-size: 16px; line-height: 23px; margin-top: 2px; }
  .section-label { position: absolute; left: 94px; font-weight: 700; color: var(--ink); }
  .section-cocktail { top: 664px; font-size: 25px; text-transform: uppercase; }
  .section-beer { top: 832px; font-size: 23px; }
  .beer-name { font-size: 17px; text-transform: uppercase; white-space: nowrap; }
  .beer-lines { font-size: 16px; line-height: 23px; }
</style>
</head>
<body>
  <main class="menu-page">
    <div class="drink-photo" role="img" aria-label="Photo of two iced cocktails with lemon slices on a bar"></div>
    <div class="accent accent-squiggle" role="img" aria-label="Hand-drawn squiggle decoration"></div>
    <div class="accent accent-splash" role="img" aria-label="Splash decoration"></div>
    <div class="accent accent-spiral" role="img" aria-label="Hand-drawn spiral decoration"></div>
    <div class="accent accent-drops" role="img" aria-label="Droplet decoration"></div>

    <h1 class="brand-name">Tall Pine<br>Bistro</h1>
    <h2 class="specials-title">weekly specials</h2>

    <section class="menu-item" style="top:428px">
      <div class="item-line"><span class="item-name">Chicken Filo</span><span class="item-leader"></span><span class="item-price">$24</span></div>
      <p class="item-desc">Creamy Chicken with Pinenuts, wrapped in Filo Pastry.<br>Served with Side Salad &amp; Zulu Sauce</p>
    </section>

    <section class="menu-item" style="top:541px">
      <div class="item-line"><span class="item-name">Minestrone Soup</span><span class="item-leader"></span><span class="item-price">$8</span></div>
      <p class="item-desc">Served with Garlic Bread</p>
    </section>

    <h3 class="section-label section-cocktail">Cocktail Special</h3>

    <section class="menu-item" style="top:720px">
      <div class="item-line"><span class="item-name">Passionista</span><span class="item-leader"></span><span class="item-price">$17</span></div>
      <p class="item-desc">Vodka, Passionfruit Pulp, Mango Puree<br>Top up with Ginger &amp; Lemon Kombucha</p>
    </section>

    <h3 class="section-label section-beer">Craft Beer Special</h3>

    <section class="menu-item" style="top:884px">
      <div class="item-line"><span class="beer-name">Copper Gecko</span><span class="item-leader"></span><span class="item-price">$10</span></div>
      <p class="beer-lines">SUN BURST<br>Tropical Pale Ale<br>4.8% Alc.</p>
    </section>
  </main>
</body>
</html>
```